Web Design Project

Current website needs stylish revamping www.trel-ika.com!!!! The look and font should be playful while showing maybe wings, shoes or something that is sexy yet confident for women to wear. The line is a division of a larger company and trademarked under their umbrella entity.

The website should have a clean, trendy and possibly modern look. Important project with hopeful long term business relation ship.

The slogan is also playful...
brr-ivo - made to glide, never pause
or
brr-ivo, quick in the stride (hence the idea of wings in the title or website)

brr-ivo...., shh, shoes be seen, not heard, light, ect.
Updates

Payment is now guaranteed- we appreciate your work!!!!

Would also like a possible slide show for the home page!!

Not many designs submitted!!! so design away - thank you greatly :)

Kindest regards,
NormaĀ 

Reason: need a great design for this project- appreciate your help!

Elegant sexy, not trashy!!!

also more clean, sophisticated and modern look- not too busy!!!
clients are high end
thank you so much!!
NormaĀ 

Target Market(s)

successful, working women

Industry/Entity Type

Business

Requirements
Must have
• Must be clean, buyer and user friendly and embody a sexy feel. Possibly bold colors or mix of neutral beige with black.

```html
<!DOCTYPE html>
<html lang="en">
<head>
<meta charset="utf-8">
<title>brr-ivo – Home</title>
<link rel="stylesheet" href="https://fonts.googleapis.com/css2?family=Oswald:wght@300;400;500&family=Arimo:wght@400;700&display=swap">
<style>
  :root {
    --black: #000000;
    --beige: #f6dcc0;
    --beige-deep: #efd0ae;
    --logo: #dcc4a4;
    --grey-field: #3d3d3d;
    --grey-link: #6f6f6f;
    --taupe: #b9aa92;
    --wall: #e4e4e2;
    --wall-shade: #c9c9c6;
    --floor: #d9d9d7;
    --floor-light: #ececea;
    --skin: #c9a487;
    --shoe: #2a2a2a;
    --style-bar: rgba(60, 60, 60, 0.62);
    --white: #ffffff;
    --button: #e9d6bd;
  }
  * { box-sizing: border-box; margin: 0; padding: 0; }
  html, body { width: 1200px; height: 642px; overflow: hidden; background: var(--black); }
  body { position: relative; font-family: "Arimo", Arial, sans-serif; }

  .site-header { position: absolute; left: 0; top: 0; width: 1200px; height: 117px; background: var(--black); }
  .account-tab { position: absolute; left: 580px; top: 0; width: 514px; height: 18px; }
  .account-tab svg { position: absolute; inset: 0; }
  .account-links { position: absolute; left: 50px; top: 3px; display: flex; gap: 16px; font-size: 11px; color: #222; }
  .account-links span:nth-child(6) { margin-left: -4px; }
  .account-links span:last-child { margin-left: 8px; }

  .brand { position: absolute; left: 107px; top: 18px; }
  .brand-name { font-family: "Oswald", sans-serif; font-weight: 300; font-size: 54px; line-height: 54px; color: var(--logo); letter-spacing: 1px; }
  .brand-tagline { margin-top: 2px; font-family: "Arimo", sans-serif; font-weight: 700; font-size: 11px; letter-spacing: 1.2px; color: var(--logo); }

  .search-field { position: absolute; left: 884px; top: 45px; width: 204px; height: 24px; border-radius: 4px; background: var(--grey-field); }
  .search-help { position: absolute; left: 897px; top: 74px; font-size: 11.5px; font-weight: 700; color: var(--grey-link); }

  .main-nav { position: absolute; left: 0; top: 117px; width: 1200px; height: 31px; background: linear-gradient(var(--beige), var(--beige-deep)); }
  .main-nav span { position: absolute; top: 2px; font-family: "Oswald", sans-serif; font-size: 16.5px; color: var(--black); transform: scaleX(0.9); transform-origin: left; }

  .hero { position: absolute; left: 0; top: 148px; width: 1200px; height: 419px; overflow: hidden;
    background:
      linear-gradient(90deg, transparent 0%, transparent 44%, rgba(201,164,135,0.55) 52%, rgba(42,42,42,0.35) 63%, rgba(201,164,135,0.45) 70%, rgba(42,42,42,0.3) 75%, transparent 82%, transparent 100%),
      linear-gradient(180deg, var(--wall) 0%, var(--wall-shade) 38%, var(--floor) 42%, var(--floor-light) 100%); }
  .style-bar { position: absolute; left: 0; top: 0; width: 1200px; height: 40px; background: var(--style-bar); }
  .style-bar span { position: absolute; top: 1px; font-family: "Oswald", sans-serif; font-size: 25px; color: var(--white); transform: scaleX(0.88); transform-origin: left; }
  .style-bar svg { position: absolute; left: 279px; top: 10px; }
  .hero-headline { position: absolute; left: 108px; top: 362px; font-family: "Oswald", sans-serif; font-weight: 400; font-size: 37px; letter-spacing: 19px; color: #111; }

  .newsletter-bar { position: absolute; left: 0; top: 567px; width: 1200px; height: 47px; background: var(--black); }
  .newsletter-title { position: absolute; left: 110px; top: 1px; font-family: "Oswald", sans-serif; font-size: 27px; color: var(--logo); transform: scaleX(0.95); transform-origin: left; }
  .field { position: absolute; top: 11px; height: 26px; border-radius: 3px; background: var(--grey-field); font-size: 11px; color: #d8d8d8; padding: 6px 10px; }
  .subscribe { position: absolute; left: 736px; top: 10px; width: 109px; height: 27px; border-radius: 3px; background: linear-gradient(#f6e8d4, var(--button)); font-size: 13px; font-weight: 700; color: #111; text-align: center; line-height: 27px; letter-spacing: 0.5px; }
  .follow { position: absolute; left: 912px; top: 6px; font-family: "Oswald", sans-serif; font-size: 19px; color: var(--logo); transform: scaleX(0.9); transform-origin: left; }
  .social { position: absolute; top: 10px; width: 28px; height: 28px; border-radius: 50%; background: #4a4a4a; }

  .site-footer { position: absolute; left: 0; top: 614px; width: 1200px; height: 28px; background: var(--taupe); font-size: 11px; color: #1a1a1a; text-align: center; line-height: 28px; padding-right: 20px; }
</style>
</head>
<body>
  <header class="site-header">
    <div class="account-tab">
      <svg width="514" height="18" viewBox="0 0 514 18"><polygon points="0,0 514,0 514,18 38,18" fill="#f6dcc0"/></svg>
      <nav class="account-links">
        <span>My Account</span><span>Order Status</span><span>Wish Lists</span><span>Gift Certificates</span><span>View Cart</span><span>Login</span><span>Sign Up</span>
      </nav>
    </div>
    <div class="brand">
      <div class="brand-name">brr-ivo</div>
      <div class="brand-tagline">MADE TO GLIDE, NEVER PAUSE</div>
    </div>
    <div class="search-field"></div>
    <div class="search-help">Advanced Search | Search Tips</div>
  </header>

  <nav class="main-nav">
    <span style="left:130px">Home</span>
    <span style="left:230px">Collections</span>
    <span style="left:353px">No More Noise</span>
    <span style="left:492px">About Us</span>
    <span style="left:603px">Reviews</span>
    <span style="left:710px">Blog</span>
    <span style="left:798px">Press</span>
    <span style="left:896px">Stores</span>
    <span style="left:1000px">Contact Us</span>
  </nav>

  <section class="hero" role="img" aria-label="Photo of a woman's crossed legs wearing black strappy peep-toe heels, seated on a white bench in a pale grey room">
    <div class="style-bar">
      <span style="left:108px">CHOOSE BY STYLE</span>
      <svg width="18" height="20" viewBox="0 0 18 20"><polyline points="3,2 13,10 3,18" fill="none" stroke="#000" stroke-width="5"/></svg>
      <span style="left:362px">BOOTIES</span>
      <span style="left:515px">FLATS</span>
      <span style="left:645px">PUMPS</span>
      <span style="left:787px">SLINGBACKS</span>
      <span style="left:997px">VIEW ALL</span>
    </div>
    <div class="hero-headline">QUICK IN THE STRIDE</div>
  </section>

  <section class="newsletter-bar">
    <div class="newsletter-title">Our Newsletter</div>
    <div class="field" style="left:268px;width:226px">Your First Name:</div>
    <div class="field" style="left:504px;width:225px">Your Email Address:</div>
    <div class="subscribe">SUBSCRIBE</div>
    <div class="follow">FOLLOW US :</div>
    <div class="social" style="left:1002px"></div>
    <div class="social" style="left:1043px"></div>
  </section>

  <footer class="site-footer">Copyright 2012 Brr-ivo. Shoe Care Shoe Size Chart Terms and Conditions FREE Shipping and Returns</footer>
</body>
</html>
```